Broschüre für Sicherheitsdienstleistungen
Zielgruppe
Sicherheitsunternehmen
Hallo,
Wir möchten gerne eine Broschüre (ca. 12 Seiten) gestalten lassen wo alle unsere verschiedene Dienstleistungen Beschrieben werden und unser unternehmen vorgestellt wird an den Kunden.
Als Hard copy Version von unsere neue Seite : http://vlm.kartenwerkstatt.de
Das Design soll Freundlich und Modern Gestaltet werden.
Farbtöne gerne in Weiss und Dunkel Blau
Produktdetails :
Rückendrahtheftung links, 4/4-farbig (beidseitiger Druck, CMYK)
ab 250 g wird der Umschlag zusätzlich genutet
Veredelung Umschlag
beidseitiger UV-Lack glänzend
Format
DIN A4 (21 x 29,7 cm)
Details: Hochformat
Seitenanzahl ca. 10 - 12 (Excl. Umschlag)
Material Umschlag
250g Bilderdruck glänzend
New Website Design :
http://vlm.kartenwerkstatt.de

```html
<!DOCTYPE html>
<html lang="de">
<head>
<meta charset="utf-8">
<title>VLM Schutzgruppe Hamburg – Broschüre</title>
<link href="https://fonts.googleapis.com/css2?family=Roboto+Condensed:wght@300;400;700&family=Open+Sans:wght@400;600;700&display=swap" rel="stylesheet">
<style>
:root{
  --navy:#2d4a8a;
  --navy-dark:#1f3468;
  --navy-soft:rgba(45,74,138,.9);
  --blue-mid:#4a6aac;
  --blue-light:#8ea5d2;
  --text:#3a3a3a;
  --paper:#ffffff;
  --stage:#e4e4e4;
}
*{box-sizing:border-box;margin:0;padding:0}
html,body{width:1200px;height:4402px;overflow:hidden;background:#fff}
body{font-family:"Open Sans",Arial,sans-serif;color:var(--text)}
.stage{position:absolute;left:137px;top:168px;width:945px;height:4192px;background:var(--stage);display:flex;flex-direction:column}
.scene{height:698px;display:flex;align-items:center;justify-content:center}
.spread{display:flex;box-shadow:0 10px 28px rgba(0,0,0,.22)}
.page{position:relative;width:360px;height:510px;background:var(--paper);overflow:hidden}
.page.single{box-shadow:0 10px 28px rgba(0,0,0,.22)}
.spread .page:first-child::after{content:"";position:absolute;top:0;right:0;bottom:0;width:14px;background:linear-gradient(90deg,rgba(0,0,0,0),rgba(0,0,0,.16));pointer-events:none}
.spread .page:last-child::after{content:"";position:absolute;top:0;left:0;bottom:0;width:14px;background:linear-gradient(270deg,rgba(0,0,0,0),rgba(0,0,0,.16));pointer-events:none}
.photo{position:absolute}
.display{font-family:"Roboto Condensed",Arial,sans-serif;text-transform:uppercase;line-height:1.02;color:#fff}
.display .light{font-weight:300}
.display .bold{font-weight:700}
.tag-box{position:absolute;background:var(--navy-soft);padding:8px 12px}

/* fliesstext in spalten */
.flow{position:absolute;column-count:2;column-gap:12px;column-fill:auto;overflow:hidden}
.flow.single-col{column-count:1}
.body-text{font-size:6.6px;line-height:1.42;text-align:justify;margin-bottom:4px;hyphens:auto}
.subhead{font-family:"Roboto Condensed",Arial,sans-serif;font-weight:700;font-size:7.2px;line-height:1.2;color:var(--navy);text-transform:uppercase;margin:5px 0 3px;break-after:avoid}
.head-box{position:absolute;background:var(--navy);color:#fff;font-family:"Roboto Condensed",Arial,sans-serif;font-weight:700;text-transform:uppercase;padding:6px 10px;line-height:1.15}

/* titel */
.cover .logo-panel{position:absolute;left:0;top:34px;width:60%;height:200px;background:var(--navy);display:flex;flex-direction:column;align-items:center;justify-content:center;gap:8px}
.brand-mark{width:34px;height:34px;background:#fff}
.brand-name{font-family:"Roboto Condensed",Arial,sans-serif;font-weight:400;font-size:12px;color:#fff;text-align:center;text-transform:uppercase;letter-spacing:.5px;line-height:1.3}
.cover .eye{left:52%;top:0;width:48%;height:250px;background:radial-gradient(circle at 60% 55%,#7fc3e6 0 8%,#2b6aa8 14%,#16325f 40%,#0d1c3a 100%)}
.cover .headline{left:0;top:232px;width:78%;padding:14px 18px}
.cover .headline .display{font-size:25px}
.cover .tagline{position:absolute;left:24px;top:430px;font-family:"Roboto Condensed",Arial,sans-serif;font-weight:700;font-size:13px;color:var(--navy)}
.cover .rule{position:absolute;left:24px;right:24px;top:420px;height:1px;background:var(--blue-light)}

.section-title .display{font-size:22px}
.quote{position:absolute;left:24px;top:250px;width:210px;border:1.5px solid #fff;background:rgba(31,52,104,.55);padding:10px 12px}
.quote .display{font-size:18px}
.quote .source{font-size:6px;color:#dfe6f5;margin-top:6px}
.slogan{position:absolute;font-family:"Roboto Condensed",Arial,sans-serif;font-weight:700;font-size:17px;color:var(--navy);text-transform:uppercase;line-height:1.05}

.contact-block{position:absolute;left:0;top:40px;width:100%;height:440px;background:var(--blue-mid)}
.contact-band{position:absolute;right:0;top:40px;width:55%;height:34px;background:var(--navy-dark);display:flex;align-items:center;padding-left:14px}
.contact-band .display{font-size:16px}
</style>
</head>
<body>
<main class="stage">

  <!-- Titelseite -->
  <section class="scene">
    <article class="page single cover">
      <div class="photo eye" role="img" aria-label="Nahaufnahme eines Auges mit digitalen Linien in Blautönen"></div>
      <div class="logo-panel">
        <div class="brand-mark"></div>
        <div class="brand-name">VLM Schutzgruppe<br>Hamburg GmbH</div>
      </div>
      <div class="tag-box headline">
        <p class="display"><span class="bold">Sicherheit</span><br><span class="light">und</span> <span class="bold">Kompetenz</span><br><span class="light">europaweit</span> <span class="bold">aus</span><br><span class="bold">einer Hand</span></p>
      </div>
      <div class="rule"></div>
      <p class="tagline">Ihr Sicherheitsdienst bundesweit seit 1999</p>
    </article>
  </section>

  <!-- Über uns -->
  <section class="scene">
    <div class="spread">
      <article class="page">
        <div class="photo" style="inset:0;background:linear-gradient(180deg,#6b86b8 0%,#3c5a92 40%,#1b2d55 70%,#c9933e 100%)" role="img" aria-label="Skyline einer Großstadt in der Abenddämmerung"></div>
        <div class="tag-box section-title" style="right:0;top:30px;width:150px"><p class="display"><span class="light">Über</span><br><span class="bold">uns</span></p></div>
        <div class="tag-box" style="left:0;bottom:36px;width:270px">
          <p class="body-text" style="color:#fff;font-size:7.4px;font-weight:600;text-transform:uppercase;margin:0">Auf unsere Erfahrung können Sie bauen: Wir planen Schutzkonzepte individuell, prüfen Risiken sorgfältig und setzen nur Personal ein, das regelmäßig geschult wird.</p>
        </div>
      </article>
      <article class="page">
        <div class="head-box" style="left:22px;top:22px;width:170px;font-size:10px">VLM Solid GmbH – Ihr zuverlässiger Sicherheitsdienst</div>
        <div class="flow" style="left:22px;right:22px;top:72px;height:416px">
          <p class="body-text">Seit vielen Jahren schützen wir Menschen, Gebäude und Werte mit geschulten Fachkräften, klaren Abläufen und moderner Technik. Kunden aus Industrie, Handel und Verwaltung vertrauen auf unsere Erfahrung und Verlässlichkeit.</p>
          <p class="body-text">Unsere Teams arbeiten rund um die Uhr, stimmen jeden Einsatz persönlich mit Ihnen ab und berichten zuverlässig über jede Auffälligkeit vor Ort. So behalten Sie jederzeit den Überblick über Ihre Sicherheit.</p>
          <p class="subhead">Unsere Leistungen im Überblick</p>
          <p class="body-text">Wir planen Schutzkonzepte individuell, prüfen Risiken sorgfältig und setzen nur Personal ein, das regelmäßig geschult und überprüft wird. Diskretion, Pünktlichkeit und Höflichkeit sind für uns selbstverständlich.</p>
          <p class="body-text">Ob kurzfristiger Auftrag oder langfristige Betreuung: Ein fester Ansprechpartner begleitet Sie von der ersten Beratung bis zur Umsetzung und passt die Maßnahmen flexibel an neue Anforderungen an.</p>
          <p class="body-text">Modernste Kommunikationstechnik verbindet unsere Einsatzkräfte mit der Leitstelle. Im Ernstfall reagieren wir schnell, informieren alle Beteiligten und leiten die notwendigen Schritte ohne Zeitverlust ein.</p>
          <p class="subhead">Qualität, die man sieht</p>
          <p class="body-text">Seit vielen Jahren schützen wir Menschen, Gebäude und Werte mit geschulten Fachkräften, klaren Abläufen und moderner Technik. Kunden aus Industrie, Handel und Verwaltung vertrauen auf unsere Erfahrung und Verlässlichkeit.</p>
          <p class="body-text">Unsere Teams arbeiten rund um die Uhr, stimmen jeden Einsatz persönlich mit Ihnen ab und berichten zuverlässig über jede Auffälligkeit vor Ort. So behalten Sie jederzeit den Überblick über Ihre Sicherheit.</p>
          <p class="body-text">Wir planen Schutzkonzepte individuell, prüfen Risiken sorgfältig und setzen nur Personal ein, das regelmäßig geschult und überprüft wird. Diskretion, Pünktlichkeit und Höflichkeit sind für uns selbstverständlich.</p>
          <p class="subhead">Ihr Vorteil mit uns</p>
          <p class="body-text">Ob kurzfristiger Auftrag oder langfristige Betreuung: Ein fester Ansprechpartner begleitet Sie von der ersten Beratung bis zur Umsetzung und passt die Maßnahmen flexibel an neue Anforderungen an.</p>
          <p class="body-text">Modernste Kommunikationstechnik verbindet unsere Einsatzkräfte mit der Leitstelle. Im Ernstfall reagieren wir schnell, informieren alle Beteiligten und leiten die notwendigen Schritte ohne Zeitverlust ein.</p>
          <p class="subhead">Europaweit im Einsatz</p>
          <p class="body-text">Seit vielen Jahren schützen wir Menschen, Gebäude und Werte mit geschulten Fachkräften, klaren Abläufen und moderner Technik. Kunden aus Industrie, Handel und Verwaltung vertrauen auf unsere Erfahrung und Verlässlichkeit.</p>
          <p class="body-text">Unsere Teams arbeiten rund um die Uhr, stimmen jeden Einsatz persönlich mit Ihnen ab und berichten zuverlässig über jede Auffälligkeit vor Ort. So behalten Sie jederzeit den Überblick über Ihre Sicherheit.</p>
          <p class="body-text">Wir planen Schutzkonzepte individuell, prüfen Risiken sorgfältig und setzen nur Personal ein, das regelmäßig geschult und überprüft wird. Diskretion, Pünktlichkeit und Höflichkeit sind für uns selbstverständlich.</p>
          <p class="body-text">Ob kurzfristiger Auftrag oder langfristige Betreuung: Ein fester Ansprechpartner begleitet Sie von der ersten Beratung bis zur Umsetzung und passt die Maßnahmen flexibel an neue Anforderungen an.</p>
        </div>
      </article>
    </div>
  </section>

  <!-- Personenschutz / High Risk -->
  <section class="scene">
    <div class="spread">
      <article class="page">
        <div class="photo" style="left:0;top:0;width:62%;height:140px;background:linear-gradient(135deg,#3b5e9c,#c98a3a 60%,#6b4a2a)" role="img" aria-label="Personenschützer begleitet eine Person"></div>
        <div class="tag-box section-title" style="left:62%;top:24px;width:38%;padding:8px 10px"><p class="display" style="font-size:18px"><span class="light">Personen</span><br><span class="bold">schutz</span></p></div>
        <div class="flow" style="left:22px;right:22px;top:152px;height:338px">
          <p class="subhead">VLM Solid – Personenschutz mit Erfahrung</p>
          <p class="body-text">Seit vielen Jahren schützen wir Menschen, Gebäude und Werte mit geschulten Fachkräften, klaren Abläufen und moderner Technik. Kunden aus Industrie, Handel und Verwaltung vertrauen auf unsere Erfahrung und Verlässlichkeit.</p>
          <p class="body-text">Unsere Teams arbeiten rund um die Uhr, stimmen jeden Einsatz persönlich mit Ihnen ab und berichten zuverlässig über jede Auffälligkeit vor Ort. So behalten Sie jederzeit den Überblick über Ihre Sicherheit.</p>
          <p class="body-text">Wir planen Schutzkonzepte individuell, prüfen Risiken sorgfältig und setzen nur Personal ein, das regelmäßig geschult und überprüft wird. Diskretion, Pünktlichkeit und Höflichkeit sind für uns selbstverständlich.</p>
          <p class="subhead">Diskret und unauffällig</p>
          <p class="body-text">Ob kurzfristiger Auftrag oder langfristige Betreuung: Ein fester Ansprechpartner begleitet Sie von der ersten Beratung bis zur Umsetzung und passt die Maßnahmen flexibel an neue Anforderungen an.</p>
          <p class="body-text">Modernste Kommunikationstechnik verbindet unsere Einsatzkräfte mit der Leitstelle. Im Ernstfall reagieren wir schnell, informieren alle Beteiligten und leiten die notwendigen Schritte ohne Zeitverlust ein.</p>
          <p class="body-text">Seit vielen Jahren schützen wir Menschen, Gebäude und Werte mit geschulten Fachkräften, klaren Abläufen und moderner Technik. Kunden aus Industrie, Handel und Verwaltung vertrauen auf unsere Erfahrung und Verlässlichkeit.</p>
          <p class="subhead">Ihr Vorteil mit uns</p>
          <p class="body-text">Unsere Teams arbeiten rund um die Uhr, stimmen jeden Einsatz persönlich mit Ihnen ab und berichten zuverlässig über jede Auffälligkeit vor Ort. So behalten Sie jederzeit den Überblick über Ihre Sicherheit.</p>
          <p class="body-text">Wir planen Schutzkonzepte individuell, prüfen Risiken sorgfältig und setzen nur Personal ein, das regelmäßig geschult und überprüft wird. Diskretion, Pünktlichkeit und Höflichkeit sind für uns selbstverständlich.</p>
          <p class="body-text">Ob kurzfristiger Auftrag oder langfristige Betreuung: Ein fester Ansprechpartner begleitet Sie von der ersten Beratung bis zur Umsetzung und passt die Maßnahmen flexibel an neue Anforderungen an.</p>
          <p class="body-text">Modernste Kommunikationstechnik verbindet unsere Einsatzkräfte mit der Leitstelle. Im Ernstfall reagieren wir schnell, informieren alle Beteiligten und leiten die notwendigen Schritte ohne Zeitverlust ein.</p>
        </div>
      </article>
      <article class="page">
        <div class="flow single-col" style="left:22px;width:138px;top:22px;height:468px">
          <p class="subhead">VLM Solid – Schutz in Risikogebieten</p>
          <p class="body-text">Seit vielen Jahren schützen wir Menschen, Gebäude und Werte mit geschulten Fachkräften, klaren Abläufen und moderner Technik. Kunden aus Industrie, Handel und Verwaltung vertrauen auf unsere Erfahrung und Verlässlichkeit.</p>
          <p class="body-text">Unsere Teams arbeiten rund um die Uhr, stimmen jeden Einsatz persönlich mit Ihnen ab und berichten zuverlässig über jede Auffälligkeit vor Ort. So behalten Sie jederzeit den Überblick über Ihre Sicherheit.</p>
          <p class="subhead">Unsere Leistungen im Überblick</p>
          <p class="body-text">Wir planen Schutzkonzepte individuell, prüfen Risiken sorgfältig und setzen nur Personal ein, das regelmäßig geschult und überprüft wird. Diskretion, Pünktlichkeit und Höflichkeit sind für uns selbstverständlich.</p>
          <p class="body-text">Ob kurzfristiger Auftrag oder langfristige Betreuung: Ein fester Ansprechpartner begleitet Sie von der ersten Beratung bis zur Umsetzung und passt die Maßnahmen flexibel an neue Anforderungen an.</p>
          <p class="body-text">Modernste Kommunikationstechnik verbindet unsere Einsatzkräfte mit der Leitstelle. Im Ernstfall reagieren wir schnell, informieren alle Beteiligten und leiten die notwendigen Schritte ohne Zeitverlust ein.</p>
          <p class="subhead">Sicher ans Ziel</p>
          <p class="body-text">Seit vielen Jahren schützen wir Menschen, Gebäude und Werte mit geschulten Fachkräften, klaren Abläufen und moderner Technik. Kunden aus Industrie, Handel und Verwaltung vertrauen auf unsere Erfahrung und Verlässlichkeit.</p>
          <p class="body-text">Unsere Teams arbeiten rund um die Uhr, stimmen jeden Einsatz persönlich mit Ihnen ab und berichten zuverlässig über jede Auffälligkeit vor Ort. So behalten Sie jederzeit den Überblick über Ihre Sicherheit.</p>
          <p class="body-text">Wir planen Schutzkonzepte individuell, prüfen Risiken sorgfältig und setzen nur Personal ein, das regelmäßig geschult und überprüft wird. Diskretion, Pünktlichkeit und Höflichkeit sind für uns selbstverständlich.</p>
        </div>
        <div class="photo" style="left:172px;top:0;right:0;bottom:0;background:linear-gradient(180deg,#0f5fa8 0%,#3d8fd0 55%,#9cc7ea 80%,#1e2a3a 100%)" role="img" aria-label="Kletterer an einer Felswand vor blauem Himmel"></div>
        <div class="tag-box section-title" style="left:172px;bottom:50px;width:150px"><p class="display"><span class="light">High Risk</span><br><span class="bold">Security</span></p></div>
      </article>
    </div>
  </section>

  <!-- Brandsicherheit / Zitat -->
  <section class="scene">
    <div class="spread">
      <article class="page">
        <div class="flow" style="left:22px;right:22px;top:22px;height:270px">
          <p class="subhead">VLM Solid – Brandsicherheitswache</p>
          <p class="body-text">Seit vielen Jahren schützen wir Menschen, Gebäude und Werte mit geschulten Fachkräften, klaren Abläufen und moderner Technik. Kunden aus Industrie, Handel und Verwaltung vertrauen auf unsere Erfahrung und Verlässlichkeit.</p>
          <p class="subhead">Die zuverlässige Brandwache für Veranstaltungen</p>
          <p class="body-text">Unsere Teams arbeiten rund um die Uhr, stimmen jeden Einsatz persönlich mit Ihnen ab und berichten zuverlässig über jede Auffälligkeit vor Ort. So behalten Sie jederzeit den Überblick über Ihre Sicherheit.</p>
          <p class="body-text">Wir planen Schutzkonzepte individuell, prüfen Risiken sorgfältig und setzen nur Personal ein, das regelmäßig geschult und überprüft wird. Diskretion, Pünktlichkeit und Höflichkeit sind für uns selbstverständlich.</p>
          <p class="subhead">Brandschutzhelfer der VLM Solid</p>
          <p class="body-text">Ob kurzfristiger Auftrag oder langfristige Betreuung: Ein fester Ansprechpartner begleitet Sie von der ersten Beratung bis zur Umsetzung und passt die Maßnahmen flexibel an neue Anforderungen an.</p>
          <p class="body-text">Modernste Kommunikationstechnik verbindet unsere Einsatzkräfte mit der Leitstelle. Im Ernstfall reagieren wir schnell, informieren alle Beteiligten und leiten die notwendigen Schritte ohne Zeitverlust ein.</p>
          <p class="subhead">Gute Gründe für unsere Brandwache</p>
          <p class="body-text">Seit vielen Jahren schützen wir Menschen, Gebäude und Werte mit geschulten Fachkräften, klaren Abläufen und moderner Technik. Kunden aus Industrie, Handel und Verwaltung vertrauen auf unsere Erfahrung und Verlässlichkeit.</p>
          <p class="body-text">Unsere Teams arbeiten rund um die Uhr, stimmen jeden Einsatz persönlich mit Ihnen ab und berichten zuverlässig über jede Auffälligkeit vor Ort. So behalten Sie jederzeit den Überblick über Ihre Sicherheit.</p>
          <p class="body-text">Wir planen Schutzkonzepte individuell, prüfen Risiken sorgfältig und setzen nur Personal ein, das regelmäßig geschult und überprüft wird. Diskretion, Pünktlichkeit und Höflichkeit sind für uns selbstverständlich.</p>
        </div>
        <div class="photo" style="left:0;bottom:0;width:100%;height:205px;background:linear-gradient(120deg,#1e2d4a,#8a2a2a 45%,#d23a2a 60%,#3a3a3a)" role="img" aria-label="Feuerwehrhelm und rote Hydranten"></div>
        <div class="tag-box section-title" style="left:0;bottom:38px;width:100%"><p class="display" style="font-size:20px"><span class="light">Brand</span><span class="bold">sicherheit</span></p></div>
      </article>
      <article class="page">
        <div class="photo" style="inset:0;background:linear-gradient(180deg,#5a6a85 0%,#b79a78 35%,#4c5a3a 65%,#2a3320 100%)" role="img" aria-label="Zwei Personen auf einem Felsvorsprung über einer Graslandschaft"></div>
        <div class="quote">
          <p class="display"><span class="light">„Ohne</span> <span class="bold">Sicherheit</span> <span class="light">ist</span><br><span class="light">keine</span> <span class="bold">Freiheit.“</span></p>
          <p class="source">Leitsatz des Hauses</p>
        </div>
      </article>
    </div>
  </section>

  <!-- Fahrerservice / Objektschutz -->
  <section class="scene">
    <div class="spread">
      <article class="page">
        <div class="flow" style="left:22px;right:22px;top:22px;height:250px">
          <p class="subhead">VLM Solid – der zuverlässige Fahrdienst</p>
          <p class="body-text">Seit vielen Jahren schützen wir Menschen, Gebäude und Werte mit geschulten Fachkräften, klaren Abläufen und moderner Technik. Kunden aus Industrie, Handel und Verwaltung vertrauen auf unsere Erfahrung und Verlässlichkeit.</p>
          <p class="subhead">Top in Form: die Fahrer der VLM Solid</p>
          <p class="body-text">Unsere Teams arbeiten rund um die Uhr, stimmen jeden Einsatz persönlich mit Ihnen ab und berichten zuverlässig über jede Auffälligkeit vor Ort. So behalten Sie jederzeit den Überblick über Ihre Sicherheit.</p>
          <p class="subhead">Zuverlässige Mitarbeiter werden geprüft</p>
          <p class="body-text">Wir planen Schutzkonzepte individuell, prüfen Risiken sorgfältig und setzen nur Personal ein, das regelmäßig geschult und überprüft wird. Diskretion, Pünktlichkeit und Höflichkeit sind für uns selbstverständlich.</p>
          <p class="subhead">VLM Solid: Ihr Security-Fahrdienst</p>
          <p class="body-text">Ob kurzfristiger Auftrag oder langfristige Betreuung: Ein fester Ansprechpartner begleitet Sie von der ersten Beratung bis zur Umsetzung und passt die Maßnahmen flexibel an neue Anforderungen an.</p>
          <p class="subhead">Professionell – und natürlich diskret</p>
          <p class="body-text">Modernste Kommunikationstechnik verbindet unsere Einsatzkräfte mit der Leitstelle. Im Ernstfall reagieren wir schnell, informieren alle Beteiligten und leiten die notwendigen Schritte ohne Zeitverlust ein.</p>
          <p class="subhead">Buchen Sie jetzt Ihren Fahrdienst</p>
          <p class="body-text">Seit vielen Jahren schützen wir Menschen, Gebäude und Werte mit geschulten Fachkräften, klaren Abläufen und moderner Technik. Kunden aus Industrie, Handel und Verwaltung vertrauen auf unsere Erfahrung und Verlässlichkeit.</p>
          <p class="body-text">Unsere Teams arbeiten rund um die Uhr, stimmen jeden Einsatz persönlich mit Ihnen ab und berichten zuverlässig über jede Auffälligkeit vor Ort. So behalten Sie jederzeit den Überblick über Ihre Sicherheit.</p>
        </div>
        <div class="photo" style="left:0;bottom:0;width:58%;height:220px;background:linear-gradient(160deg,#6d7684,#2b313b 60%,#15191f)" role="img" aria-label="Fahrer am Steuer einer Limousine"></div>
        <div class="tag-box section-title" style="left:0;bottom:40px;width:58%"><p class="display"><span class="light">Fahrer</span><br><span class="bold">Service</span></p></div>
        <p class="slogan" style="left:222px;bottom:90px">Vertrauen<br>ist gut,<br>Kontrolle<br>ist jedoch<br>besser.</p>
      </article>
      <article class="page">
        <div class="photo" style="right:0;top:30px;width:190px;height:190px;background:linear-gradient(150deg,#2f4f8f,#7a93c2 55%,#c9ccd4)" role="img" aria-label="Überwachungskamera an einer Gebäudewand"></div>
        <div class="tag-box section-title" style="right:0;top:30px;width:190px"><p class="display"><span class="light">Objekt</span><br><span class="bold">schutz</span></p></div>
        <div class="head-box" style="left:22px;top:30px;width:130px;font-size:9px">VLM Solid – der zuverlässige Objektschutz</div>
        <div class="flow single-col" style="left:22px;width:134px;top:76px;height:146px">
          <p class="body-text">Sicherheit spielt für viele Unternehmen eine große Rolle. Wir planen Schutzkonzepte individuell, prüfen Risiken sorgfältig und setzen nur Personal ein, das regelmäßig geschult und überprüft wird.</p>
          <p class="subhead">Objektschutz für Gebäude von Unternehmen</p>
          <p class="body-text">Ob kurzfristiger Auftrag oder langfristige Betreuung: Ein fester Ansprechpartner begleitet Sie von der ersten Beratung bis zur Umsetzung und passt die Maßnahmen flexibel an neue Anforderungen an.</p>
          <p class="body-text">Modernste Kommunikationstechnik verbindet unsere Einsatzkräfte mit der Leitstelle und sorgt für schnelle Reaktion.</p>
        </div>
        <div class="flow" style="left:22px;right:22px;top:234px;height:256px">
          <p class="subhead">Der umfassende Service von der VLM Solid</p>
          <p class="body-text">Seit vielen Jahren schützen wir Menschen, Gebäude und Werte mit geschulten Fachkräften, klaren Abläufen und moderner Technik. Kunden aus Industrie, Handel und Verwaltung vertrauen auf unsere Erfahrung und Verlässlichkeit.</p>
          <p class="body-text">Unsere Teams arbeiten rund um die Uhr, stimmen jeden Einsatz persönlich mit Ihnen ab und berichten zuverlässig über jede Auffälligkeit vor Ort. So behalten Sie jederzeit den Überblick über Ihre Sicherheit.</p>
          <p class="subhead">Objektschutz für Institutionen aller Art</p>
          <p class="body-text">Wir planen Schutzkonzepte individuell, prüfen Risiken sorgfältig und setzen nur Personal ein, das regelmäßig geschult und überprüft wird. Diskretion, Pünktlichkeit und Höflichkeit sind für uns selbstverständlich.</p>
          <p class="body-text">Ob kurzfristiger Auftrag oder langfristige Betreuung: Ein fester Ansprechpartner begleitet Sie von der ersten Beratung bis zur Umsetzung und passt die Maßnahmen flexibel an neue Anforderungen an.</p>
          <p class="subhead">Buchen Sie jetzt den Objektschutz von der VLM Solid</p>
          <p class="body-text">Modernste Kommunikationstechnik verbindet unsere Einsatzkräfte mit der Leitstelle. Im Ernstfall reagieren wir schnell, informieren alle Beteiligten und leiten die notwendigen Schritte ohne Zeitverlust ein.</p>
          <p class="body-text">Seit vielen Jahren schützen wir Menschen, Gebäude und Werte mit geschulten Fachkräften, klaren Abläufen und moderner Technik. Kunden aus Industrie, Handel und Verwaltung vertrauen auf unsere Erfahrung und Verlässlichkeit.</p>
          <p class="body-text">Unsere Teams arbeiten rund um die Uhr, stimmen jeden Einsatz persönlich mit Ihnen ab und berichten zuverlässig über jede Auffälligkeit vor Ort. So behalten Sie jederzeit den Überblick über Ihre Sicherheit.</p>
        </div>
      </article>
    </div>
  </section>

  <!-- Rückseite + Titel -->
  <section class="scene">
    <div class="spread">
      <article class="page">
        <div class="contact-block"></div>
        <div class="contact-band"><p class="display"><span class="light">Kon</span><span class="bold">takt</span></p></div>
      </article>
      <article class="page cover">
        <div class="photo eye" role="img" aria-label="Nahaufnahme eines Auges mit digitalen Linien in Blautönen"></div>
        <div class="logo-panel">
          <div class="brand-mark"></div>
          <div class="brand-name">VLM Schutzgruppe<br>Hamburg GmbH</div>
        </div>
        <div class="tag-box headline">
          <p class="display"><span class="bold">Sicherheit</span><br><span class="light">und</span> <span class="bold">Kompetenz</span><br><span class="light">europaweit</span> <span class="bold">aus</span><br><span class="bold">einer Hand</span></p>
        </div>
        <div class="rule"></div>
        <p class="tagline">Ihr Sicherheitsdienst bundesweit seit 1999</p>
      </article>
    </div>
  </section>

</main>
</body>
</html>
```